web page layout, style , color, font & flow design

We are developing a single page application. The SPA (single page application) will display natural gas pipeline flow data once the customer logs on. The customer has a choice of the region, the pipeline, the zone on the pipeline, whether the point is a delivery point or receipt point and the state the pipeline flows through.
we have jumpstarted the project and are attaching a pdf of the same.

we are using mockingbird for the wireframe. any designer is free to use this tool to make changes.

A mockingbird wireframe link is added below. you are free to use it and to make changes. please save the changed wireframe in a different name

we are looking for inputs on layout, style , color, font & flow.

A logo jpg file has also been attached.

Target Market(s)

this single web page is going to be used by natural gas traders and schedulers day in and day out. the application is more of business to business corporate application.

Industry/Entity Type

Delivery

Requirements
Must have
• layout ,flow, size, color, font , ease of use.

```html
<!DOCTYPE html>
<html lang="en">
<head>
<meta charset="utf-8">
<title>Metrix Flow – Pipeline Flow Data</title>
<link href="https://fonts.googleapis.com/css2?family=Arimo:wght@400;700&display=swap" rel="stylesheet">
<style>
:root{
  --blue:#1f7ae0;
  --blue-dark:#0d5cb6;
  --link:#0b4fa8;
  --text:#333;
  --muted:#777;
  --line:#e2e2e2;
  --row-alt:#e3e3e3;
  --green:#6cb33f;
  --page:#fff;
}
*{box-sizing:border-box;margin:0;padding:0}
html,body{width:1200px;height:1011px;overflow:hidden;background:var(--page);font-family:"Arimo",Arial,sans-serif;color:var(--text)}
.page{position:relative;width:1200px;height:1011px;background:linear-gradient(#f7f7f7,#fff 110px)}
.abs{position:absolute}

.brand{left:66px;top:40px;display:flex;align-items:center;gap:8px;font-size:20px;font-weight:700;color:var(--blue-dark)}
.brand-dot{width:22px;height:22px;border-radius:50%;background:var(--green)}

.contact{right:66px;top:13px;font-size:9px;color:#666;display:flex;gap:14px}
.userbar{right:71px;top:40px;font-size:11px;display:flex;gap:10px;color:#ccc}
.userbar a{color:var(--link);text-decoration:none;display:flex;align-items:center;gap:4px}

.search-tabs{left:360px;top:46px;font-size:11px;display:flex;gap:28px}
.search-tabs span{color:var(--link)}
.search-tabs .current{color:#222}
.search-box{left:352px;top:71px;width:782px;height:30px;border:1px solid #ddd;border-radius:2px;background:#fff}
.search-box svg{position:absolute;right:10px;top:7px}

.sidebar{left:47px;top:121px;width:286px;border:1px solid var(--line);background:#fff}
.sidebar-head{height:36px;background:linear-gradient(#1a6fd1,#0d5cb6);color:#fff;font-size:13px;display:flex;align-items:center;padding:0 14px;gap:10px}
.sidebar-head .chev{margin-left:auto}
.pipe{height:45.6px;border-top:1px solid var(--line);display:flex;align-items:center;padding:0 14px;font-size:11px;font-weight:700;color:var(--link);background:linear-gradient(#fff,#f6f6f6)}
.pipe .plus{margin-left:auto}

.regions{left:352px;top:121px;display:flex;gap:6px}
.region{width:112px;height:36px;background:var(--blue);color:#fff;font-size:13px;display:flex;align-items:center;justify-content:center}
.region.active{background:var(--blue-dark)}

.panel{left:352px;top:157px;width:782px;height:751px;border:1px solid var(--line);background:#fff}
.sort-label{left:20px;top:25px;font-size:11px;color:#222}
.rule{left:12px;width:757px;height:1px;background:var(--line)}
.filter-label{font-size:11px;color:#444;line-height:13px}
.select{height:26px;border:1px solid #ddd;font-size:11px;color:#555;padding:0 8px;display:flex;align-items:center;background:#fff}
.select .arrow{position:absolute;right:0;top:0;width:26px;height:24px;border-left:1px solid #ddd;display:flex;align-items:center;justify-content:center}

.grid{left:12px;top:140px;width:757px;border-collapse:collapse;table-layout:fixed;font-size:11px}
.grid th{height:28px;font-weight:400;color:#555;border:1px solid var(--line);background:#fff;font-size:11px}
.grid .spacer td{height:10px;border:none;background:#fff}
.grid td{height:29.4px;color:var(--muted);padding-left:18px;border-left:1px solid var(--line);border-right:1px solid var(--line)}
.grid tbody tr:nth-child(even) td{background:var(--row-alt);border-color:#fff}
.grid tbody tr:first-child td{border-top:1px solid var(--line)}

.pager{right:20px;top:727px;font-size:11px;display:flex;gap:14px}
.pager .off{color:#aaa}
.pager span{color:var(--link)}

.footer-rule{left:49px;top:941px;width:1085px;height:1px;background:var(--line)}
.footer{left:49px;top:958px;font-size:10px;color:#777;display:flex;gap:20px}
.footer i{font-style:normal;color:#bbb}
</style>
</head>
<body>
<div class="page">

  <div class="abs brand"><span class="brand-dot"></span>Metrix Flow</div>

  <div class="abs contact">
    <span>480 Harbor Point Avenue, 6th Floor, Easton, Ohio 43210</span>
    <span>(555) 012-3480</span>
  </div>
  <div class="abs userbar">
    <a href="#"><svg width="10" height="10"><circle cx="5" cy="5" r="5" fill="#6cb33f"/><text x="5" y="8" font-size="8" text-anchor="middle" fill="#fff" font-family="Arial">?</text></svg>Help</a>|
    <a href="#">Logout</a>|
    <a href="#"><svg width="9" height="10"><circle cx="4.5" cy="3" r="2.5" fill="#6cb33f"/><path d="M0 10a4.5 4.5 0 0 1 9 0z" fill="#6cb33f"/></svg>Dana</a>
  </div>

  <div class="abs search-tabs"><span class="current">Quick Search</span><span>State</span><span>Other</span></div>
  <div class="abs search-box">
    <svg width="18" height="18" viewBox="0 0 18 18"><circle cx="7.5" cy="7.5" r="6" fill="none" stroke="#ddd" stroke-width="2"/><path d="M12 12l5 5" stroke="#ddd" stroke-width="2"/></svg>
  </div>

  <nav class="abs sidebar">
    <div class="sidebar-head">
      <svg width="16" height="12"><rect x="0" y="5" width="16" height="5" fill="#fff"/><rect x="6" y="1" width="4" height="4" fill="#fff"/></svg>
      Pipelines
      <svg class="chev" width="14" height="8"><path d="M1 1l6 6 6-6" fill="none" stroke="#fff" stroke-width="1.3"/></svg>
    </div>
    <div class="pipe">Aldermoor<svg class="plus" width="12" height="12"><circle cx="6" cy="6" r="6" fill="#c8c8c8"/><path d="M6 3v6M3 6h6" stroke="#fff" stroke-width="1.5"/></svg></div>
    <div class="pipe">CRT<svg class="plus" width="12" height="12"><circle cx="6" cy="6" r="6" fill="#c8c8c8"/><path d="M6 3v6M3 6h6" stroke="#fff" stroke-width="1.5"/></svg></div>
    <div class="pipe">Dunmore<svg class="plus" width="12" height="12"><circle cx="6" cy="6" r="6" fill="#c8c8c8"/><path d="M6 3v6M3 6h6" stroke="#fff" stroke-width="1.5"/></svg></div>
    <div class="pipe">Easter Bay NG<svg class="plus" width="12" height="12"><circle cx="6" cy="6" r="6" fill="#c8c8c8"/><path d="M6 3v6M3 6h6" stroke="#fff" stroke-width="1.5"/></svg></div>
    <div class="pipe">East Ridge NG<svg class="plus" width="12" height="12"><circle cx="6" cy="6" r="6" fill="#c8c8c8"/><path d="M6 3v6M3 6h6" stroke="#fff" stroke-width="1.5"/></svg></div>
    <div class="pipe">Emberline Gas<svg class="plus" width="12" height="12"><circle cx="6" cy="6" r="6" fill="#c8c8c8"/><path d="M6 3v6M3 6h6" stroke="#fff" stroke-width="1.5"/></svg></div>
    <div class="pipe">Equiflow Inc<svg class="plus" width="12" height="12"><circle cx="6" cy="6" r="6" fill="#c8c8c8"/><path d="M6 3v6M3 6h6" stroke="#fff" stroke-width="1.5"/></svg></div>
    <div class="pipe">Granite Vale Gas<svg class="plus" width="12" height="12"><circle cx="6" cy="6" r="6" fill="#c8c8c8"/><path d="M6 3v6M3 6h6" stroke="#fff" stroke-width="1.5"/></svg></div>
    <div class="pipe">Ironwood<svg class="plus" width="12" height="12"><circle cx="6" cy="6" r="6" fill="#c8c8c8"/><path d="M6 3v6M3 6h6" stroke="#fff" stroke-width="1.5"/></svg></div>
    <div class="pipe">Seaboard &amp; North East<svg class="plus" width="12" height="12"><circle cx="6" cy="6" r="6" fill="#c8c8c8"/><path d="M6 3v6M3 6h6" stroke="#fff" stroke-width="1.5"/></svg></div>
    <div class="pipe">Meridian Pipeline<svg class="plus" width="12" height="12"><circle cx="6" cy="6" r="6" fill="#c8c8c8"/><path d="M6 3v6M3 6h6" stroke="#fff" stroke-width="1.5"/></svg></div>
    <div class="pipe">Northfield Fuel Gas Supply Corp<svg class="plus" width="12" height="12"><circle cx="6" cy="6" r="6" fill="#c8c8c8"/><path d="M6 3v6M3 6h6" stroke="#fff" stroke-width="1.5"/></svg></div>
    <div class="pipe">Porter NG<svg class="plus" width="12" height="12"><circle cx="6" cy="6" r="6" fill="#c8c8c8"/><path d="M6 3v6M3 6h6" stroke="#fff" stroke-width="1.5"/></svg></div>
    <div class="pipe">St. Clement Gas<svg class="plus" width="12" height="12"><circle cx="6" cy="6" r="6" fill="#c8c8c8"/><path d="M6 3v6M3 6h6" stroke="#fff" stroke-width="1.5"/></svg></div>
    <div class="pipe">Tanager Gas<svg class="plus" width="12" height="12"><circle cx="6" cy="6" r="6" fill="#c8c8c8"/><path d="M6 3v6M3 6h6" stroke="#fff" stroke-width="1.5"/></svg></div>
    <div class="pipe">Transvale<svg class="plus" width="12" height="12"><circle cx="6" cy="6" r="6" fill="#c8c8c8"/><path d="M6 3v6M3 6h6" stroke="#fff" stroke-width="1.5"/></svg></div>
  </nav>

  <div class="abs regions">
    <div class="region active">NorthEast</div>
    <div class="region">MidWest</div>
    <div class="region">SouthEast</div>
    <div class="region">SouthWest</div>
    <div class="region">Central</div>
    <div class="region">West</div>
  </div>

  <section class="abs panel">
    <div class="abs sort-label">Sort Results by:</div>
    <div class="abs rule" style="top:47px"></div>

    <div class="abs filter-label" style="left:21px;top:75px">Location Type:</div>
    <div class="abs select" style="left:102px;top:68px;width:145px">All<span class="arrow"><svg width="10" height="7"><path d="M0 0h10L5 7z" fill="#1f7ae0"/></svg></span></div>
    <div class="abs filter-label" style="left:267px;top:75px">Interstate pipeline</div>
    <div class="abs select" style="left:361px;top:68px;width:145px">All<span class="arrow"><svg width="10" height="7"><path d="M0 0h10L5 7z" fill="#1f7ae0"/></svg></span></div>
    <div class="abs filter-label" style="left:534px;top:77px">Pipeline zones:</div>
    <div class="abs select" style="left:614px;top:70px;width:145px">Zones<span class="arrow"><svg width="10" height="7"><path d="M0 0h10L5 7z" fill="#1f7ae0"/></svg></span></div>
    <div class="abs rule" style="top:115px"></div>

    <table class="abs grid">
      <colgroup><col style="width:74px"><col style="width:90px"><col style="width:92px"><col style="width:97px"><col style="width:102px"><col style="width:87px"><col style="width:91px"><col style="width:124px"></colgroup>
      <thead>
        <tr><th>gasday</th><th>location</th><th>loc_Name</th><th>Flow_Ind</th><th>L oc_Desc</th><th>Op_cap</th><th>Sch_cap</th><th>Op_avail_cap</th></tr>
        <tr class="spacer"><td colspan="8"></td></tr>
      </thead>
      <tbody>
        <tr><td>Item 1</td><td>Item 2</td><td>Item 3</td><td>Item 4</td><td>Item 5</td><td>Item 6</td><td>Item 7</td><td>Item 8</td></tr>
        <tr><td>Item 1</td><td>Item 2</td><td>Item 3</td><td>Item 4</td><td>Item 5</td><td>Item 6</td><td>Item 7</td><td>Item 8</td></tr>
        <tr><td>Item 1</td><td>Item 2</td><td>Item 3</td><td>Item 4</td><td>Item 5</td><td>Item 6</td><td>Item 7</td><td>Item 8</td></tr>
        <tr><td>Item 1</td><td>Item 2</td><td>Item 3</td><td>Item 4</td><td>Item 5</td><td>Item 6</td><td>Item 7</td><td>Item 8</td></tr>
        <tr><td>Item 1</td><td>Item 2</td><td>Item 3</td><td>Item 4</td><td>Item 5</td><td>Item 6</td><td>Item 7</td><td>Item 8</td></tr>
        <tr><td>Item 1</td><td>Item 2</td><td>Item 3</td><td>Item 4</td><td>Item 5</td><td>Item 6</td><td>Item 7</td><td>Item 8</td></tr>
        <tr><td>Item 1</td><td>Item 2</td><td>Item 3</td><td>Item 4</td><td>Item 5</td><td>Item 6</td><td>Item 7</td><td>Item 8</td></tr>
        <tr><td>Item 1</td><td>Item 2</td><td>Item 3</td><td>Item 4</td><td>Item 5</td><td>Item 6</td><td>Item 7</td><td>Item 8</td></tr>
        <tr><td>Item 1</td><td>Item 2</td><td>Item 3</td><td>Item 4</td><td>Item 5</td><td>Item 6</td><td>Item 7</td><td>Item 8</td></tr>
        <tr><td>Item 1</td><td>Item 2</td><td>Item 3</td><td>Item 4</td><td>Item 5</td><td>Item 6</td><td>Item 7</td><td>Item 8</td></tr>
        <tr><td>Item 1</td><td>Item 2</td><td>Item 3</td><td>Item 4</td><td>Item 5</td><td>Item 6</td><td>Item 7</td><td>Item 8</td></tr>
        <tr><td>Item 1</td><td>Item 2</td><td>Item 3</td><td>Item 4</td><td>Item 5</td><td>Item 6</td><td>Item 7</td><td>Item 8</td></tr>
        <tr><td>Item 1</td><td>Item 2</td><td>Item 3</td><td>Item 4</td><td>Item 5</td><td>Item 6</td><td>Item 7</td><td>Item 8</td></tr>
        <tr><td>Item 1</td><td>Item 2</td><td>Item 3</td><td>Item 4</td><td>Item 5</td><td>Item 6</td><td>Item 7</td><td>Item 8</td></tr>
        <tr><td>Item 1</td><td>Item 2</td><td>Item 3</td><td>Item 4</td><td>Item 5</td><td>Item 6</td><td>Item 7</td><td>Item 8</td></tr>
        <tr><td>Item 1</td><td>Item 2</td><td>Item 3</td><td>Item 4</td><td>Item 5</td><td>Item 6</td><td>Item 7</td><td>Item 8</td></tr>
        <tr><td>Item 1</td><td>Item 2</td><td>Item 3</td><td>Item 4</td><td>Item 5</td><td>Item 6</td><td>Item 7</td><td>Item 8</td></tr>
        <tr><td>Item 1</td><td>Item 2</td><td>Item 3</td><td>Item 4</td><td>Item 5</td><td>Item 6</td><td>Item 7</td><td>Item 8</td></tr>
      </tbody>
    </table>

    <div class="abs pager"><span class="off">1</span><span>2</span><span>&gt;</span></div>
  </section>

  <div class="abs footer-rule"></div>
  <footer class="abs footer">
    <span>Home</span><i>|</i><span>DataServices</span><i>|</i><span>About Us</span><i>|</i><span>Contact Us</span>
  </footer>
</div>
</body>
</html>
```